Harborline Telecom Print Ad

I'm looking for a four panel piece for Harborline Telecom similar to the attached ad for QuietEar that is a clean, not too busy look using the elements from Harborline Telecom's website:

https://www.harborlinetelecom.example/

We like to include impactful imagery on the cover, more details on the service like a quote from their Founder, a "How it works" section, and other simple icons to communicate Harborline Telecom's benefits in the middle two panels, and testimonials on the back.

Here are a few other 4 panel creative examples for creative inspiration:

https://pages.leafviewer.example/view/471903586/

```html
<!DOCTYPE html>
<html lang="en">
<head>
<meta charset="utf-8">
<title>Harborline Telecom – Four Panel Print Ad</title>
<link href="https://fonts.googleapis.com/css2?family=Poppins:wght@400;500;600;700&family=Open+Sans:wght@400;600;700&display=swap" rel="stylesheet">
<style>
:root{
  --stage:#e6e6fa;
  --white:#ffffff;
  --navy:#14145a;
  --navy-deep:#0f1050;
  --ink:#1b1b2e;
  --violet:#7b7cf5;
  --violet-soft:#8b84f7;
  --blue:#5b6cf0;
  --blue-tile:#6475f3;
  --cyan:#5fdcf8;
  --sky:#dcefff;
  --name-blue:#7d96ff;
  --star:#f5821f;
  --line:#9d9cf0;
}
*{box-sizing:border-box;margin:0;padding:0}
html,body{width:1200px;height:576px;overflow:hidden;background:var(--stage)}
body{position:relative;font-family:"Open Sans",sans-serif;color:var(--ink)}
.panel{position:absolute;top:91px;width:259px;height:401px;overflow:hidden}
.panel--cover{left:45px;background:var(--white)}
.panel--story{left:330px;background:var(--white)}
.panel--benefits{left:619px;width:257px;background:var(--blue)}
.panel--reviews{left:903px;background:var(--navy-deep)}

.brand-box{position:absolute;left:31px;top:-2px;width:205px;height:44px;background:var(--white);border:1.5px solid var(--line);border-top:none;border-radius:0 0 12px 12px;display:flex;align-items:center;justify-content:center;gap:6px}
.brand-dot{width:7px;height:7px;border-radius:50%;background:var(--violet)}
.brand-name{font-family:"Poppins",sans-serif;font-weight:600;font-size:15px;color:var(--ink);letter-spacing:.2px}

/* cover */
.cover-photo{position:absolute;left:0;top:42px;width:259px;height:260px;background:radial-gradient(circle at 60% 40%,#f3e2d6 0%,#cfe3c4 45%,#e9efe6 100%)}
.cover-arch{position:absolute;left:-40px;top:262px;width:339px;height:240px;background:var(--navy);border-radius:50% 50% 0 0}
.feature-circle{position:absolute;top:226px;width:74px;height:74px;border-radius:50%;border:3px solid var(--white);background:radial-gradient(circle,#eaf4ff,#bcd9f7)}
.cover-title{position:absolute;left:0;width:259px;top:302px;text-align:center;font-family:"Poppins",sans-serif;font-weight:700;font-size:17.5px;line-height:19px;color:var(--white)}
.cover-sub{position:absolute;left:0;width:259px;top:344px;text-align:center;font-family:"Poppins",sans-serif;font-size:9px;line-height:10.5px;color:var(--white)}
.cover-url{position:absolute;left:28px;top:377px;width:205px;height:30px;border-radius:15px;background:var(--blue);color:var(--white);font-family:"Poppins",sans-serif;font-weight:500;font-size:10.5px;text-align:center;padding-top:6px}

/* story */
.story-intro{position:absolute;left:20px;width:219px;top:55px;text-align:center;font-size:8.6px;line-height:10.3px}
.story-intro strong{font-weight:700}
.quote-card{position:absolute;left:27px;top:122px;width:205px;height:166px;border:1.5px solid var(--line);border-radius:12px;background:var(--white)}
.founder-photo{position:absolute;left:106px;top:97px;width:50px;height:50px;border-radius:50%;background:linear-gradient(160deg,#e8ecf6,#b9c3d8);border:2px solid var(--white)}
.quote-mark{position:absolute;right:12px;top:22px;font-family:"Poppins",sans-serif;font-weight:700;font-size:30px;line-height:30px;color:#22c6f0}
.founder-name{position:absolute;left:0;width:205px;top:32px;font-size:7px;text-align:left;padding-left:44px}
.founder-name b{font-weight:700}
.quote-text{position:absolute;left:12px;top:47px;width:181px;font-size:6.9px;line-height:8.5px;text-align:justify}
.quote-close{position:absolute;left:12px;top:135px;width:181px;text-align:center;font-weight:700;font-size:6.9px;line-height:8px}
.values-band{position:absolute;left:0;top:298px;width:259px;height:103px;background:var(--violet-soft)}
.values-pill{position:absolute;left:95px;top:14px;width:70px;height:17px;border-radius:9px;background:var(--ink);color:var(--white);font-family:"Poppins",sans-serif;font-weight:600;font-size:9.5px;text-align:center;line-height:17px}
.values-list{position:absolute;left:8px;top:36px;width:243px;text-align:center;color:var(--white);font-size:7.4px;line-height:9.5px}
.trust-strip{position:absolute;left:27px;top:68px;width:204px;height:40px;background:var(--white);border-radius:12px 12px 0 0}
.trust-caption{position:absolute;left:0;top:5px;width:204px;text-align:center;font-size:4.8px;color:#9a9ab0}
.trust-marks{position:absolute;left:14px;top:15px;display:flex;gap:10px}
.trust-mark{width:22px;height:11px;border-radius:2px;background:#c9c9d8}

/* benefits */
.cyan-zone{position:absolute;left:0;top:250px;width:257px;height:151px;background:var(--cyan)}
.call-curve{position:absolute;left:-40px;top:196px;width:337px;height:102px;border-radius:0 0 50% 50%;background:var(--blue)}
.benefits-title{position:absolute;left:0;width:257px;top:8px;text-align:center;font-family:"Poppins",sans-serif;font-weight:600;font-size:15px;color:var(--white)}
.benefit-grid{position:absolute;left:16px;top:34px;width:228px;display:grid;grid-template-columns:repeat(3,72px);grid-auto-rows:90px;gap:6px}
.benefit{border:1px solid rgba(255,255,255,.55);border-radius:8px;background:var(--blue-tile);text-align:center;color:var(--white);font-size:7.6px;line-height:9.2px;padding:7px 3px 0}
.benefit svg{display:block;margin:0 auto 6px;width:37px;height:37px}
.guarantee{position:absolute;left:16px;top:227px;width:228px;height:17px;border-radius:9px;background:var(--ink);color:var(--white);font-family:"Poppins",sans-serif;font-weight:600;font-size:8.3px;text-align:center;line-height:17px}
.call-lead{position:absolute;left:0;width:257px;top:253px;text-align:center;font-family:"Poppins",sans-serif;font-weight:600;font-size:10px;color:var(--white)}
.call-number{position:absolute;left:0;width:257px;top:266px;display:flex;justify-content:center;align-items:center;gap:8px;font-family:"Poppins",sans-serif;font-weight:600;font-size:16px;color:var(--white)}
.call-icon{width:16px;height:16px;border-radius:50%;background:var(--ink);display:flex;align-items:center;justify-content:center}
.wireless-photo{position:absolute;left:15px;top:303px;width:108px;height:98px;border-radius:50% 50% 0 0;background:linear-gradient(170deg,#f5d7b8,#e7b68c 60%,#ffffff)}
.wireless-title{position:absolute;left:133px;width:112px;top:308px;text-align:center;font-family:"Poppins",sans-serif;font-weight:600;font-size:10px;line-height:11.6px;color:var(--ink)}
.wireless-rule{position:absolute;left:137px;top:344px;width:104px;border-top:1.5px dotted var(--ink)}
.wireless-list{position:absolute;left:137px;top:352px;list-style:none;font-family:"Poppins",sans-serif;font-size:8.2px;line-height:11.8px;color:var(--ink)}
.wireless-list li{display:flex;align-items:center;gap:4px}
.tick{width:9px;height:9px;border-radius:50%;background:var(--blue);display:inline-flex;align-items:center;justify-content:center}

/* reviews */
.reviews-title{position:absolute;left:0;width:259px;top:11px;text-align:center;font-family:"Poppins",sans-serif;font-weight:600;font-size:13.5px;color:var(--white)}
.review{position:absolute;left:16px;width:228px;height:88px;border:1px solid rgba(180,190,255,.6);border-radius:8px;padding:5px 8px 0}
.review--one{top:38px}
.review--two{top:130px}
.review-name{font-family:"Poppins",sans-serif;font-weight:500;font-size:10px;line-height:11px;color:var(--name-blue)}
.review-text{font-size:6.8px;line-height:8.6px;color:var(--white);text-align:justify}
.review-stars{position:absolute;right:8px;bottom:5px;color:var(--star);font-size:12px;letter-spacing:.5px}
.badges{position:absolute;left:16px;top:226px;display:flex;gap:5px}
.badge{width:56px;height:17px;border-radius:3px;background:var(--white)}
.badge--dark{background:#1d2a6b;border:1px solid #ffffff}
.reviews-scene{position:absolute;left:0;top:270px;width:259px;height:131px;background:linear-gradient(160deg,var(--navy-deep) 0%,#3145c8 45%,#4d63ef 100%)}
</style>
</head>
<body>

<section class="panel panel--cover">
  <div class="cover-photo" role="img" aria-label="Smiling woman talking on a cordless home phone in a bright room"></div>
  <div class="cover-arch"></div>
  <div class="feature-circle" style="left:15px" role="img" aria-label="Wireless home phone base unit"></div>
  <div class="feature-circle" style="left:95px" role="img" aria-label="Cordless home phone handset"></div>
  <div class="feature-circle" style="left:173px" role="img" aria-label="Cell tower broadcasting signal"></div>
  <div class="brand-box"><span class="brand-dot"></span><span class="brand-name">harborline telecom</span></div>
  <h1 class="cover-title">Simple. Reliable.<br>Phone Service</h1>
  <p class="cover-sub">Modern landline &amp; wireless phone<br>service that doesn't require internet</p>
  <div class="cover-url">www.harborlinetelecom.example</div>
</section>

<section class="panel panel--story">
  <div class="brand-box"><span class="brand-dot"></span><span class="brand-name">harborline telecom</span></div>
  <p class="story-intro">Harborline Telecom is a venture-backed, Northgate Accelerator graduate with a simple mission: <strong>make the phone more powerful.</strong></p>
  <div class="quote-card">
    <span class="quote-mark">“</span>
    <p class="founder-name"><b>Daniel Porter</b> - Founder &amp; CEO</p>
    <p class="quote-text">I started Harborline Telecom to build a different kind of landline phone service company. We don't nickel and dime you with hidden fees. We make it easy for you to actually reach a real person when you have a problem. We don't tie you up in long contracts, or discontinue your service when it's no longer “profitable” to serve you with copper wire service. And we don't require you to have fast, reliable internet, just to make a call.</p>
    <p class="quote-close">I built Harborline Telecom to make it easy, safe, and reliable to stay connected with your family and friends.</p>
  </div>
  <div class="founder-photo" role="img" aria-label="Portrait of the founder"></div>
  <div class="values-band">
    <div class="values-pill">Our values</div>
    <p class="values-list">Curiosity | Efficiency in Everything | Bias Toward Action |<br>Transparency | Founder Mindset | Caring Mentality</p>
    <div class="trust-strip">
      <p class="trust-caption">Trusted in 10,000+ homes and businesses including</p>
      <div class="trust-marks"><span class="trust-mark"></span><span class="trust-mark"></span><span class="trust-mark"></span><span class="trust-mark"></span><span class="trust-mark"></span><span class="trust-mark"></span></div>
    </div>
  </div>
</section>

<section class="panel panel--benefits">
  <div class="cyan-zone"></div>
  <div class="call-curve"></div>
  <h2 class="benefits-title">Benefits</h2>
  <div class="benefit-grid">
    <div class="benefit"><svg viewBox="0 0 40 40"><circle cx="20" cy="20" r="19" fill="#dcefff"/><g fill="none" stroke="#4a5ef0" stroke-width="2.4" stroke-linecap="round"><path d="M9 17a16 16 0 0 1 22 0"/><path d="M13 21a10 10 0 0 1 14 0"/><path d="M17 25a4 4 0 0 1 6 0"/><path d="M11 30L29 11"/></g></svg>No internet<br>required</div>
    <div class="benefit"><svg viewBox="0 0 40 40"><circle cx="20" cy="20" r="19" fill="#dcefff"/><circle cx="20" cy="20" r="12" fill="#ffffff"/><g fill="#e0354a"><rect x="9" y="12" width="22" height="2.5"/><rect x="8" y="17" width="24" height="2.5"/><rect x="8" y="22" width="24" height="2.5"/><rect x="10" y="27" width="20" height="2.5"/></g><rect x="9" y="9" width="11" height="10" fill="#2c3f9e"/></svg>Unlimited<br>nationwide<br>calling</div>
    <div class="benefit"><svg viewBox="0 0 40 40"><circle cx="20" cy="20" r="19" fill="#dcefff"/><path d="M11 23v-3a9 9 0 0 1 18 0v3" fill="none" stroke="#4a5ef0" stroke-width="2.6"/><rect x="9" y="21" width="5" height="9" rx="2" fill="#4a5ef0"/><rect x="26" y="21" width="5" height="9" rx="2" fill="#4a5ef0"/></svg>Customer<br>support you can<br>actually reach</div>
    <div class="benefit"><svg viewBox="0 0 40 40"><circle cx="20" cy="20" r="19" fill="#dcefff"/><g fill="#4a5ef0"><circle cx="14" cy="12" r="2.3"/><circle cx="20" cy="12" r="2.3"/><circle cx="26" cy="12" r="2.3"/><circle cx="14" cy="18" r="2.3"/><circle cx="20" cy="18" r="2.3"/><circle cx="26" cy="18" r="2.3"/><circle cx="14" cy="24" r="2.3"/><circle cx="20" cy="24" r="2.3"/><circle cx="26" cy="24" r="2.3"/><circle cx="20" cy="30" r="2.3"/></g></svg>Get a new,<br>local number</div>
    <div class="benefit"><svg viewBox="0 0 40 40"><circle cx="20" cy="20" r="19" fill="#dcefff"/><g fill="none" stroke="#4a5ef0" stroke-width="2.4" stroke-linecap="round"><circle cx="20" cy="22" r="9"/><path d="M20 22l4-4"/><path d="M17 10h6"/><path d="M8 16a12 12 0 0 1 3-4"/></g></svg>30-second<br>setup</div>
    <div class="benefit"><svg viewBox="0 0 40 40"><circle cx="20" cy="20" r="19" fill="#dcefff"/><path d="M23 8L13 22h6l-2 10 10-14h-6z" fill="#4a5ef0"/></svg>Works during<br>power outages</div>
  </div>
  <div class="guarantee">Guaranteed coverage or your money back</div>
  <p class="call-lead">Call our landline specialists at</p>
  <div class="call-number"><span class="call-icon"><svg width="10" height="10" viewBox="0 0 24 24"><path d="M6.6 10.8a15 15 0 0 0 6.6 6.6l2.2-2.2a1 1 0 0 1 1-.25 11.4 11.4 0 0 0 3.6.6 1 1 0 0 1 1 1V20a1 1 0 0 1-1 1A17 17 0 0 1 3 4a1 1 0 0 1 1-1h3.5a1 1 0 0 1 1 1c0 1.25.2 2.45.6 3.6a1 1 0 0 1-.25 1z" fill="#ffffff"/></svg></span>800-555-0142</div>
  <div class="wireless-photo" role="img" aria-label="Smiling woman holding a yellow phone handset"></div>
  <p class="wireless-title">Wireless service backed by nationwide carriers</p>
  <div class="wireless-rule"></div>
  <ul class="wireless-list">
    <li><span class="tick"><svg width="6" height="6" viewBox="0 0 10 10"><path d="M2 5l2 2 4-4" fill="none" stroke="#fff" stroke-width="1.8"/></svg></span>Basic landline for home</li>
    <li><span class="tick"><svg width="6" height="6" viewBox="0 0 10 10"><path d="M2 5l2 2 4-4" fill="none" stroke="#fff" stroke-width="1.8"/></svg></span>Cell Plans</li>
    <li><span class="tick"><svg width="6" height="6" viewBox="0 0 10 10"><path d="M2 5l2 2 4-4" fill="none" stroke="#fff" stroke-width="1.8"/></svg></span>Business Landline</li>
  </ul>
</section>

<section class="panel panel--reviews">
  <h2 class="reviews-title">our customers love us</h2>
  <article class="review review--one">
    <h3 class="review-name">Maple Hollow Farm</h3>
    <p class="review-text">Harborline Telecom offered me a friendly neighborhood phone company equivalent when no other utility was available in my area. The representatives are honest and concise. What they advertise is what you get. No extra plans or fees. The quality is clear and an equal trade off from traditional landline service...</p>
    <span class="review-stars">★★★★★</span>
  </article>
  <article class="review review--two">
    <h3 class="review-name">Linda Marsh</h3>
    <p class="review-text">If you need to port over your landline and your provider won't do it for you, then you need this company. It was a smooth transition and my mom now gets to keep her phone number that she has had for over 30 years. Had to move her to an assisted living and being without a phone to all her friends was a BIG concern for me...</p>
    <span class="review-stars">★★★★★</span>
  </article>
  <div class="badges"><span class="badge badge--dark"></span><span class="badge badge--dark"></span><span class="badge badge--dark"></span><span class="badge"></span></div>
  <div class="reviews-scene" role="img" aria-label="Isometric desk with a wireless phone base plugged into the wall and a cordless phone"></div>
</section>

</body>
</html>
```